I need a feather flag designed for my business which states " HELICOPTER RIDES" and possibly adding my logo to them. This will be used for my helicopter ride business and we can put these up to show people where the rides will be .

Industry/Entity Type

aviation

Colors
00AB8E
00BBA5
67D7C9
C6EFE9
E9F9F6
EB3D1F
EC4F4E
F09395
F8D3D4
FCEDEE

Requirements
Must have
• logo

```html
<!DOCTYPE html>
<html lang="en">
<head>
<meta charset="utf-8">
<title>Helicopter Rides Feather Flag</title>
<link rel="stylesheet" href="https://fonts.googleapis.com/css2?family=Poppins:wght@800&display=swap">
<style>
  :root {
    --backdrop: #e4e4e4;
    --flag-top: #7ac943;
    --flag-mid: #5cc0b0;
    --flag-bottom: #2a96de;
    --sleeve-top: #5fb52f;
    --sleeve-bottom: #1f7fc4;
    --ink: #2e2e2e;
    --headline: #ffffff;
    --brush: #2b2b2b;
  }
  html, body {
    margin: 0;
    padding: 0;
    width: 885px;
    height: 1200px;
    overflow: hidden;
    background: var(--backdrop);
  }
  .canvas {
    position: relative;
    width: 885px;
    height: 1200px;
    font-family: "Poppins", sans-serif;
  }
  .flag {
    position: absolute;
    left: 312px;
    top: 120px;
    width: 260px;
    height: 960px;
  }
  .flag-shape {
    position: absolute;
    inset: 0;
    width: 260px;
    height: 960px;
  }
  .brand {
    position: absolute;
    left: 147px;
    top: 360px;
    width: 0;
    height: 0;
  }
  .brand-lockup {
    position: absolute;
    left: 0;
    top: 0;
    transform: translate(-50%, -50%) rotate(-90deg);
    text-align: center;
    color: var(--ink);
    font-weight: 800;
    white-space: nowrap;
    line-height: 1;
  }
  .brand-name {
    display: block;
    font-size: 60px;
    letter-spacing: 1px;
  }
  .brand-sub {
    display: block;
    margin-top: 6px;
    font-size: 15px;
    letter-spacing: 21px;
    margin-right: -21px;
  }
  .offer {
    position: absolute;
    left: 0;
    top: 752px;
    width: 240px;
    text-align: center;
  }
  .offer-title {
    margin: 0;
    font-size: 30px;
    font-weight: 800;
    color: var(--headline);
    letter-spacing: -0.5px;
    line-height: 1.1;
  }
  .offer-tag {
    position: relative;
    display: inline-block;
    margin-top: 8px;
    padding: 2px 26px;
  }
  .offer-tag-mark {
    position: absolute;
    inset: 4px 0;
    background: var(--brush);
    border-radius: 4px;
  }
  .offer-tag-word {
    position: relative;
    font-size: 36px;
    font-weight: 800;
    line-height: 1.1;
    letter-spacing: -0.5px;
    background: linear-gradient(90deg, var(--flag-top), var(--flag-mid), var(--flag-bottom));
    -webkit-background-clip: text;
    background-clip: text;
    color: transparent;
  }
</style>
</head>
<body>
<main class="canvas">
  <section class="flag">
    <svg class="flag-shape" viewBox="0 0 260 960" aria-hidden="true">
      <defs>
        <linearGradient id="flagFill" x1="0" y1="0" x2="0" y2="1">
          <stop offset="0" stop-color="var(--flag-top)"/>
          <stop offset="0.5" stop-color="var(--flag-mid)"/>
          <stop offset="1" stop-color="var(--flag-bottom)"/>
        </linearGradient>
        <linearGradient id="sleeveFill" x1="0" y1="0" x2="0" y2="1">
          <stop offset="0" stop-color="var(--sleeve-top)"/>
          <stop offset="1" stop-color="var(--sleeve-bottom)"/>
        </linearGradient>
      </defs>
      <path d="M5 960 L5 260 C5 110 110 5 250 5 L258 5 L255 950 Q255 956 249 956 Z" fill="url(#flagFill)"/>
      <path d="M5 960 L5 260 C5 110 110 5 250 5 L258 5" fill="none" stroke="url(#sleeveFill)" stroke-width="10" stroke-linecap="round"/>
    </svg>

    <div class="brand">
      <div class="brand-lockup">
        <span class="brand-name">AEROVISTA</span>
        <span class="brand-sub">HELICOPTERS</span>
      </div>
    </div>

    <div class="offer">
      <h1 class="offer-title">HELICOPTER</h1>
      <div class="offer-tag">
        <span class="offer-tag-mark" role="img" aria-label="Dark brush stroke behind the word"></span>
        <span class="offer-tag-word">RIDES</span>
      </div>
    </div>
  </section>
</main>
</body>
</html>
```